DESSERT FLYER

We need a flyer design for desserts and drinks for our restaurant.

We use Retro/rustic as main theme

Flyer must include all images, which are attached to this project. We also named correctly for each images, so you can use for each dish's title (docx file)
Must include our logo as well.

Flyer tittle is "SWEET PLUMO"

Please see our website for reference at brickhollow.com.au

Flyer's printing size is A5 Vertical. Single Side

```html
<!DOCTYPE html>
<html lang="en">
<head>
<meta charset="utf-8">
<title>Sweet Plumo – Dessert Flyer</title>
<link rel="stylesheet" href="https://fonts.googleapis.com/css2?family=Cabin+Sketch:wght@700&family=Alegreya:wght@400;700&family=Alegreya+Sans:wght@500&display=swap">
<style>
  :root {
    --teal: #138b9a;
    --teal-wood: #3f9c97;
    --bark: #362a24;
    --bark-deep: #2b211c;
    --plank: #e9e6df;
    --plank-line: #b9b3a8;
    --grid: #3b3531;
    --cell-wood: #574236;
    --cream: #f4efe6;
    --paper-edge: #cdbfa8;
    --white: #ffffff;
  }
  * { margin: 0; padding: 0; box-sizing: border-box; }
  html, body { width: 923px; height: 1200px; overflow: hidden; background: #ffffff; }
  .flyer { position: relative; width: 923px; height: 1200px; overflow: hidden; background: var(--bark); }

  .wood-strip { position: absolute; left: 0; top: 0; width: 923px; height: 40px;
    background: repeating-linear-gradient(180deg, var(--teal-wood) 0 9px, #4aa9a3 9px 10px, var(--teal-wood) 10px 20px); }
  .torn-edge { position: absolute; left: 0; top: 14px; width: 923px; height: 40px; }

  .header { position: absolute; left: 0; top: 40px; width: 923px; height: 200px;
    background: linear-gradient(180deg, var(--bark) 0%, var(--bark-deep) 100%); }
  .title { position: absolute; left: 0; right: 0; top: 52px; text-align: center;
    font-family: "Cabin Sketch", "Arial Black", sans-serif; font-weight: 700;
    font-size: 92px; letter-spacing: 5px; color: var(--cream); line-height: 1; }

  .planks { position: absolute; left: 0; top: 240px; width: 923px; height: 702px;
    background: repeating-linear-gradient(180deg, var(--plank) 0 74px, var(--plank-line) 74px 76px, #d8d3ca 76px 78px); }

  .menu-grid { position: absolute; left: 27px; top: 262px; width: 871px; height: 650px;
    background: var(--grid); padding: 8px; display: grid;
    grid-template-columns: repeat(3, 1fr); grid-template-rows: repeat(2, 1fr); gap: 14px 16px; }
  .dish { position: relative; background: linear-gradient(180deg, var(--cell-wood), #4a382e);
    border: 2px solid #8b8179; display: flex; flex-direction: column; align-items: center; }
  .dish-photo { width: 100%; height: 186px; }
  .dish-name { flex: 1; display: flex; align-items: center; justify-content: center; text-align: center;
    font-family: "Alegreya", Georgia, serif; font-size: 21px; line-height: 1.15; color: var(--cream); padding: 0 6px; }
  .dish-name.small { font-size: 17px; }
  .price { width: 174px; height: 50px; margin-bottom: 14px; border: 2px solid var(--white);
    background: rgba(255,255,255,0.22); display: flex; align-items: center; justify-content: center;
    font-family: "Alegreya Sans", Arial, sans-serif; font-weight: 500; font-size: 28px; color: var(--white); }

  .brand { position: absolute; left: 0; right: 0; top: 1000px; display: flex; align-items: center; justify-content: center; gap: 18px; }
  .brand-dot { width: 22px; height: 22px; border-radius: 50%; background: var(--teal); }
  .brand-name { font-family: "Alegreya", Georgia, serif; font-weight: 700; font-size: 68px; letter-spacing: 4px; color: var(--teal); }

  .footer { position: absolute; left: 0; bottom: 0; width: 923px; height: 68px; background: var(--teal);
    display: flex; align-items: center; justify-content: center; }
  .web { font-family: "Alegreya", Georgia, serif; font-weight: 700; font-size: 33px; color: var(--white); }
</style>
</head>
<body>
<main class="flyer">
  <div class="wood-strip"></div>
  <svg class="torn-edge" viewBox="0 0 923 40" preserveAspectRatio="none" aria-hidden="true">
    <path d="M0 22 L60 20 L120 24 L190 19 L260 23 L330 18 L420 24 L500 20 L560 14 L620 22 L700 18 L780 23 L850 17 L923 21 L923 40 L0 40 Z" fill="var(--paper-edge)"/>
    <path d="M0 26 L70 24 L130 28 L200 23 L270 27 L340 22 L430 28 L510 24 L570 19 L630 26 L710 22 L790 27 L860 21 L923 25 L923 40 L0 40 Z" fill="var(--bark)"/>
  </svg>

  <header class="header">
    <h1 class="title">SWEET PLUMO</h1>
  </header>

  <section class="planks"></section>

  <section class="menu-grid">
    <article class="dish">
      <div class="dish-photo" role="img" aria-label="Banana fritters and pastries on a banana leaf" style="background: radial-gradient(ellipse at 50% 60%, #c98a3d 0%, #a8743a 35%, #e8e6e3 70%);"></div>
      <h2 class="dish-name">Banana Fritter with<br>Vanilla Ice-cream</h2>
      <p class="price">$6.90</p>
    </article>
    <article class="dish">
      <div class="dish-photo" role="img" aria-label="Banana sago pudding on a banana leaf" style="background: radial-gradient(ellipse at 45% 60%, #f4f4f2 0%, #dfe6dc 28%, #3f7a33 60%, #2f5e27 100%);"></div>
      <h2 class="dish-name">Banana Sago Pudding<br>with Peanut Topping</h2>
      <p class="price">$6.90</p>
    </article>
    <article class="dish">
      <div class="dish-photo" role="img" aria-label="Black sticky rice with mango pieces" style="background: linear-gradient(120deg, #4a2c4e 0%, #5b3a63 45%, #e8c23a 60%, #f2d24c 100%);"></div>
      <h2 class="dish-name">Black Sticky Rice<br>with Mango</h2>
      <p class="price">$6.90</p>
    </article>
    <article class="dish">
      <div class="dish-photo" role="img" aria-label="Fried ice-cream in a glass bowl with caramel topping" style="background: radial-gradient(ellipse at 50% 65%, #f0e2c4 0%, #d69a4a 30%, #2f4048 70%, #1f2c33 100%);"></div>
      <h2 class="dish-name small">Fried Ice-Cream with Caramel<br>Chocolate/Strawberry Topping</h2>
      <p class="price">$6.90</p>
    </article>
    <article class="dish">
      <div class="dish-photo" role="img" aria-label="Fresh young coconut drink on a wooden table" style="background: radial-gradient(ellipse at 50% 70%, #efe6cf 0%, #b7824e 35%, #7a3f22 75%, #5e2f1a 100%);"></div>
      <h2 class="dish-name">Fresh Young Coconut<br>Juice</h2>
      <p class="price">$5.50</p>
    </article>
    <article class="dish">
      <div class="dish-photo" role="img" aria-label="Vietnamese drip coffee with coffee beans on a wooden board" style="background: linear-gradient(180deg, #2a211c 0%, #5a4331 55%, #b58b5f 80%, #8a6440 100%);"></div>
      <h2 class="dish-name">Vietnamese Coffee</h2>
      <p class="price">$6.90</p>
    </article>
  </section>

  <div class="brand">
    <span class="brand-dot"></span>
    <span class="brand-name">BRICK HOLLOW</span>
  </div>

  <footer class="footer">
    <p class="web">www.brickhollow.com.au</p>
  </footer>
</main>
</body>
</html>
```